"Vantarel Inc." Needs a Logo Design and Business Card

The name of the company is "Vantarel Inc."
Our Business decription, which should appear on the front of the Business Card along with the logo and business name is:
"Boutique Global Procurement and Management Services"
We offer the following SERVICES that should be listed on the back of the Business Card :
"Consultants"
"Management"
"Business Research & Development"
"Sourcing Agent"
"Distributors"
We would like to see designs that use the colors
burnt orange and,
stainless steel
Business card designs should be innovatively modern and contemporary
Telephone number and email address should be on the back of the card
Updates
The name of the firm is "Vantarel Inc.
Industry/Entity Type
Steel
Look and feel
Each slider illustrates characteristics of the customer's brand and the style your logo design should communicate.

```html
<!DOCTYPE html>
<html lang="en">
<head>
<meta charset="UTF-8">
<title>Vantarel Inc. – Business Card</title>
<link href="https://fonts.googleapis.com/css2?family=Ubuntu:wght@400;500&display=swap" rel="stylesheet">
<style>
  :root {
    --backdrop: #d9d9d9;
    --card-light: #f7f7f5;
    --card-dark: #3a3a3a;
    --burnt-orange: #d2522a;
    --ink: #2f2f2f;
    --steel: #d6d6d6;
    --tagline: #ececec;
  }
  * { margin: 0; padding: 0; box-sizing: border-box; }
  html, body {
    width: 1200px;
    height: 900px;
    overflow: hidden;
  }
  body {
    background: var(--backdrop);
    font-family: "Ubuntu", sans-serif;
    position: relative;
  }
  .card {
    position: absolute;
    left: 250px;
    width: 700px;
    height: 390px;
    box-shadow: 0 6px 18px rgba(0,0,0,0.25);
  }
  .card--back {
    top: 45px;
    background: var(--card-light);
    border-bottom: 12px solid var(--burnt-orange);
  }
  .card--front {
    top: 465px;
    background: var(--card-dark);
  }
  .wordmark {
    display: flex;
    align-items: center;
    gap: 14px;
    font-weight: 500;
    letter-spacing: -1px;
    white-space: nowrap;
  }
  .wordmark__dot {
    border-radius: 50%;
    background: var(--burnt-orange);
    flex: none;
  }
  .card--back .wordmark {
    position: absolute;
    left: 44px;
    top: 40px;
    font-size: 58px;
    color: var(--ink);
  }
  .card--back .wordmark__dot { width: 26px; height: 26px; }
  .contact {
    position: absolute;
    left: 48px;
    top: 170px;
    color: var(--ink);
  }
  .contact__name {
    color: var(--burnt-orange);
    font-size: 26px;
    font-weight: 400;
  }
  .contact__role {
    font-size: 15px;
    margin-top: 2px;
  }
  .contact__phone,
  .contact__email {
    font-size: 22px;
  }
  .contact__phone { margin-top: 26px; }
  .contact__email { margin-top: 6px; }
  .services {
    position: absolute;
    left: 390px;
    top: 250px;
    font-size: 16px;
    line-height: 1.3;
    color: var(--ink);
  }
  .services__title {
    color: var(--burnt-orange);
    text-decoration: underline;
    font-size: 17px;
  }
  .services__list {
    list-style: none;
  }
  .services__list li span::before {
    content: "- ";
    color: var(--burnt-orange);
  }
  .services__list li span + span { margin-left: 10px; }
  .card--front .wordmark {
    position: absolute;
    left: 0;
    right: 0;
    top: 120px;
    justify-content: center;
    font-size: 80px;
    color: var(--steel);
  }
  .card--front .wordmark__dot { width: 34px; height: 34px; }
  .tagline {
    position: absolute;
    left: 0;
    right: 0;
    top: 265px;
    text-align: center;
    font-size: 19px;
    color: var(--tagline);
    letter-spacing: 0.3px;
  }
</style>
</head>
<body>
  <section class="card card--back">
    <div class="wordmark">
      <span class="wordmark__dot"></span>
      <span class="wordmark__name">Vantarel Inc.</span>
    </div>
    <div class="contact">
      <p class="contact__name">Corinne Hadley</p>
      <p class="contact__role">Senior Accountant</p>
      <p class="contact__phone">555.018.4421</p>
      <p class="contact__email">CHadley@vantarel.com</p>
    </div>
    <div class="services">
      <p class="services__title">Services:</p>
      <ul class="services__list">
        <li><span>Consultants</span><span>Management</span></li>
        <li><span>Business Research &amp; Development</span></li>
        <li><span>Sourcing Agent</span><span>Distributors</span></li>
      </ul>
    </div>
  </section>

  <section class="card card--front">
    <div class="wordmark">
      <span class="wordmark__dot"></span>
      <span class="wordmark__name">Vantarel Inc.</span>
    </div>
    <p class="tagline">Boutique Global Procurement and Management Services</p>
  </section>
</body>
</html>
```